Lantern Forge needs a business card

The logo we have uploaded is going to be the image centered on the back.
The business card color is going to be black. Increase the contrast in the logo and lettering so the grey stands out from the black and is more readable. Keep the shadow effect if you can.
On the front, the only part of the logo that should be used is the Egyptian character. We would like the following information included: Name (first last), Title, Phone number, email and company name (Lantern Forge).
The images of colored sound waves we uploaded is a concept we would like implemented on the front as well but please do not use the exact image. It is for guideline purposes.
Get creative with the empty space. We are a technology company that deals with sound and lights. Please not too busy.
Thank you, we look forward to all your submissions.

```html
<!DOCTYPE html>
<html lang="en">
<head>
<meta charset="utf-8">
<title>Lantern Forge business card</title>
<link rel="stylesheet" href="https://fonts.googleapis.com/css2?family=Open+Sans:wght@400;600&display=swap">
<style>
  :root {
    --page: #e9e6e1;
    --card-dark: #262626;
    --panel-grey: #48484a;
    --accent-red: #ee3d4a;
    --logo-grey: #8c8c8c;
    --text-light: #f2f2f2;
    --streak-a: #1c1a22;
    --streak-b: #2c2f36;
  }
  * { margin: 0; padding: 0; box-sizing: border-box; }
  html, body { width: 1200px; height: 900px; overflow: hidden; }
  body {
    background: var(--page);
    font-family: "Open Sans", Arial, sans-serif;
    position: relative;
  }
  .card {
    position: absolute;
    left: 250px;
    width: 700px;
    height: 400px;
    overflow: hidden;
    box-shadow: 0 10px 24px rgba(0,0,0,0.28);
  }
  .card-back { top: 40px; }
  .card-front { top: 470px; background: var(--card-dark); }

  .light-streaks {
    position: absolute; inset: 0;
    background:
      radial-gradient(ellipse at 30% 40%, rgba(70,50,110,0.35), transparent 60%),
      radial-gradient(ellipse at 75% 60%, rgba(40,80,60,0.3), transparent 60%),
      linear-gradient(90deg, var(--streak-a), var(--streak-b) 50%, var(--streak-a));
  }
  .logo-lockup {
    position: absolute;
    display: flex;
    align-items: center;
    gap: 14px;
    font-weight: 600;
    color: var(--logo-grey);
    letter-spacing: 1px;
    white-space: nowrap;
  }
  .logo-lockup .mark {
    width: 26px; height: 26px;
    background: var(--accent-red);
  }
  .card-back .logo-lockup {
    left: 50%; top: 50%;
    transform: translate(-50%, -50%);
    font-size: 40px;
  }
  .card-front .logo-lockup {
    left: 420px; top: 176px;
    font-size: 32px;
  }
  .card-front .logo-lockup .mark { width: 22px; height: 22px; }

  .front-graphic { position: absolute; inset: 0; }

  .contact {
    position: absolute;
    left: 38px; top: 150px;
    color: var(--text-light);
    font-size: 15px;
    line-height: 1.6;
  }
  .contact .person-name {
    color: var(--accent-red);
    font-size: 22px;
    font-weight: 600;
    line-height: 1.3;
  }
  .contact .role { margin-bottom: 12px; }
</style>
</head>
<body>

  <section class="card card-back" aria-label="Card back">
    <div class="light-streaks" role="img" aria-label="Dark background with faint coloured light streaks"></div>
    <div class="logo-lockup"><span class="mark"></span><span class="brand-name">Lantern Forge</span></div>
  </section>

  <section class="card card-front" aria-label="Card front">
    <svg class="front-graphic" width="700" height="400" viewBox="0 0 700 400">
      <defs>
        <linearGradient id="sound-glow" x1="0" y1="0" x2="0" y2="1">
          <stop offset="0" stop-color="#b44ac8"/>
          <stop offset="0.3" stop-color="#d8445a"/>
          <stop offset="0.55" stop-color="#4a6ee0"/>
          <stop offset="0.8" stop-color="#3fae5a"/>
          <stop offset="1" stop-color="#e08a3a"/>
        </linearGradient>
        <linearGradient id="sound-fade" x1="0" y1="0" x2="1" y2="0">
          <stop offset="0" stop-color="#fff" stop-opacity="1"/>
          <stop offset="1" stop-color="#fff" stop-opacity="0"/>
        </linearGradient>
        <mask id="sound-mask">
          <rect x="280" y="0" width="180" height="400" fill="url(#sound-fade)"/>
        </mask>
      </defs>
      <polygon points="0,0 280,0 390,400 0,400" fill="var(--panel-grey)"/>
      <polygon class="sound-band" role="img" aria-label="Multicoloured sound wave band along the diagonal"
               points="280,0 340,0 450,400 390,400" fill="url(#sound-glow)" opacity="0.8" mask="url(#sound-mask)"/>
      <line x1="280" y1="0" x2="390" y2="400" stroke="var(--accent-red)" stroke-width="3"/>
    </svg>

    <div class="contact">
      <p class="person-name">Mara Quill</p>
      <p class="role">Director</p>
      <p class="company">Lantern Forge</p>
      <p class="phone">214 555 0183</p>
      <p class="web">www.lanternforge.com</p>
      <p class="email">hello@lanternforge.com</p>
    </div>

    <div class="logo-lockup"><span class="mark"></span><span class="brand-name">Lantern Forge</span></div>
  </section>

</body>
</html>
```